New business card with our logo

we finalized our logo with the help of pixel harbor - now we need a business card using that logo. we are a metal service center providing raw steel and metal products for fabricating, contractors, artists, etc. we have the wording for the back of the card figured out (attached, no deviations from text please), just need help putting it all together.
Contact Information for Business Card
would like the look of steel somehow incorporated in the design ... would like the black part of the logo to be steel or silver color (the S & MORROW)
Font styles to use
Other font styles liked:
- calibri, arial, similar to those, modern looking
Colors
Designer to choose colors to be used in the design.
Requirements
Must have
- Back of card must haves are attached (no deviations from wording please).
- FRONT of card:
- logo
- address
- name
- office tel
- cell
- fax
- website
- address
Nice to have
- incorporate the look of steel or element of steel somehow
- names of the staff on front not in all caps, i.e. Tereza not TEREZA
- this industry is more industrial, not coffee or flower shop so design should be aligned with that
- design should be classic and tasteful

```html
<!DOCTYPE html>
<html lang="en">
<head>
<meta charset="utf-8">
<title>Morrow Steel – Business Card</title>
<link href="https://fonts.googleapis.com/css2?family=Roboto:wght@400;500;700&display=swap" rel="stylesheet">
<style>
  :root {
    --backdrop: #e8e6e3;
    --card: #f4f4f4;
    --steel-dark: #333436;
    --brand-blue: #0d70b8;
    --white: #ffffff;
    --text-grey: #555555;
  }
  html, body {
    margin: 0;
    padding: 0;
    width: 1200px;
    height: 960px;
    overflow: hidden;
    background: var(--backdrop);
    font-family: "Roboto", Arial, sans-serif;
  }
  .canvas {
    position: relative;
    width: 1200px;
    height: 960px;
  }
  .card {
    position: absolute;
    width: 600px;
    height: 343px;
    background: var(--card);
    box-shadow: 0 3px 8px rgba(0,0,0,0.35);
    overflow: hidden;
  }
  .card--front { left: 314px; top: 113px; }
  .card--back  { left: 311px; top: 472px; }

  .front-arc {
    position: absolute;
    inset: 0;
  }
  .brand {
    position: absolute;
    left: 43px;
    top: 37px;
    display: flex;
    align-items: center;
    gap: 12px;
  }
  .brand__dot {
    width: 34px;
    height: 34px;
    border-radius: 50%;
    background: var(--brand-blue);
  }
  .brand__name {
    font-weight: 700;
    font-size: 29px;
    color: var(--steel-dark);
    letter-spacing: 0.5px;
  }
  .person {
    position: absolute;
    left: 43px;
    top: 212px;
  }
  .person__name {
    font-weight: 700;
    font-size: 21px;
    color: var(--brand-blue);
    margin: 0;
    line-height: 1.1;
  }
  .person__role {
    font-weight: 500;
    font-size: 14px;
    color: var(--steel-dark);
    margin: 3px 0 0;
  }
  .contact {
    position: absolute;
    right: 29px;
    top: 165px;
    color: var(--white);
    font-size: 14px;
    text-align: right;
  }
  .contact__address {
    margin: 0 0 26px;
    line-height: 19px;
    font-style: normal;
  }
  .contact__list {
    list-style: none;
    margin: 0;
    padding: 0;
  }
  .contact__item {
    display: flex;
    justify-content: flex-end;
    align-items: center;
    gap: 14px;
    height: 19.5px;
  }
  .contact__icon {
    width: 13px;
    height: 13px;
    fill: var(--white);
  }

  .back-brand {
    position: absolute;
    left: 0;
    right: 0;
    top: 64px;
    display: flex;
    flex-direction: column;
    align-items: center;
  }
  .back-brand__dot {
    width: 104px;
    height: 104px;
    border-radius: 50%;
    background: var(--brand-blue);
    margin-bottom: 12px;
  }
  .back-brand__name {
    font-weight: 700;
    font-size: 41px;
    line-height: 40px;
    color: var(--steel-dark);
    text-align: center;
    letter-spacing: 0.5px;
  }
  .website {
    position: absolute;
    left: 0;
    right: 0;
    top: 299px;
    text-align: center;
    font-size: 14px;
    letter-spacing: 3.2px;
    color: var(--text-grey);
  }
</style>
</head>
<body>
<main class="canvas">

  <section class="card card--front">
    <svg class="front-arc" width="600" height="343" viewBox="0 0 600 343">
      <circle cx="587" cy="362" r="300" fill="var(--steel-dark)"/>
      <circle cx="602" cy="362" r="290" fill="var(--white)"/>
      <circle cx="604" cy="362" r="288" fill="var(--brand-blue)"/>
    </svg>

    <div class="brand">
      <span class="brand__dot"></span>
      <span class="brand__name">MORROW STEEL</span>
    </div>

    <div class="person">
      <p class="person__name">Daniel Brooks</p>
      <p class="person__role">CEO/FOUNDER</p>
    </div>

    <div class="contact">
      <address class="contact__address">2214 Foundry Road<br>Anchorage, Alaska 99502</address>
      <ul class="contact__list">
        <li class="contact__item">907 555 0142
          <svg class="contact__icon" viewBox="0 0 16 16"><path d="M3.6 1l2.6 3.2-1.5 1.6c.9 2 2.5 3.6 4.5 4.5l1.6-1.5L14 11.4 12.5 14C6.6 13.7 2.3 9.4 2 3.5z"/></svg>
        </li>
        <li class="contact__item">907 555 0187
          <svg class="contact__icon" viewBox="0 0 16 16"><path d="M4 0h8a1 1 0 011 1v14a1 1 0 01-1 1H4a1 1 0 01-1-1V1a1 1 0 011-1zm.8 2v10h6.4V2zM8 13a.8.8 0 100 1.6A.8.8 0 008 13z" fill-rule="evenodd"/></svg>
        </li>
        <li class="contact__item">907 555 0163
          <svg class="contact__icon" viewBox="0 0 16 16"><path d="M4 1h8v4H4zM1 6h14v6h-2v-2H3v2H1zm3 5h8v4H4z"/></svg>
        </li>
        <li class="contact__item">daniel@morrowsteel.com
          <svg class="contact__icon" viewBox="0 0 16 16"><path d="M1 3h14v1L8 9 1 4zm0 2.5l7 5 7-5V13H1z"/></svg>
        </li>
      </ul>
    </div>
  </section>

  <section class="card card--back">
    <div class="back-brand">
      <span class="back-brand__dot"></span>
      <span class="back-brand__name">MORROW<br>STEEL</span>
    </div>
    <p class="website">www.morrowsteel.com</p>
  </section>

</main>
</body>
</html>
```